business stationery for email layout
startup company
Simple
RT
Via G. Morelli, 17
26813 Codogno LO
Italy
Info@Tallimora.com
www.tallimora.com
minimalist, retail, fashion, technology, internet, innovative,one-step ahead, easy, intuitive, immediate, serious,credible
logo blue version
logo grey version
symbol blue version
symbol grey version

```html
<!DOCTYPE html>
<html lang="en">
<head>
<meta charset="utf-8">
<title>Tallimora business card</title>
<link href="https://fonts.googleapis.com/css2?family=Source+Sans+3:wght@400;700&display=swap" rel="stylesheet">
<style>
  :root {
    --page-bg: #e9ecf0;
    --card-bg: #ffffff;
    --navy: #1b2f86;
    --band-dark: #142a7a;
    --band-light: #2f5fc9;
    --accent-line: #5fb4e6;
    --text-grey: #55585e;
    --divider: #c9ccd2;
  }
  * { margin: 0; padding: 0; box-sizing: border-box; }
  html, body { width: 1200px; height: 780px; overflow: hidden; }
  body {
    background: var(--page-bg);
    font-family: "Source Sans 3", "Myriad Pro", Arial, sans-serif;
    position: relative;
  }
  .card {
    position: absolute;
    left: 100px; top: 90px;
    width: 1000px; height: 600px;
    background: var(--card-bg);
    border-radius: 10px 44px 44px 10px;
    box-shadow: 0 6px 22px rgba(0,0,0,0.18);
    overflow: hidden;
  }
  .card-band {
    position: absolute; left: 0; top: 0; bottom: 0;
    width: 30px;
    background: linear-gradient(180deg, var(--band-light), var(--band-dark) 55%, var(--band-light));
  }
  .card-band-line {
    position: absolute; left: 38px; top: 0; bottom: 0;
    width: 3px; background: var(--accent-line);
  }
  .brand {
    position: absolute; left: 0; right: 0; top: 105px;
    display: flex; justify-content: center; align-items: center; gap: 18px;
  }
  .brand-dot {
    width: 22px; height: 22px; border-radius: 50%;
    background: var(--navy);
  }
  .brand-name {
    font-weight: 700; font-size: 92px; letter-spacing: 1px;
    color: var(--navy); text-transform: uppercase; line-height: 1;
  }
  .divider {
    position: absolute; left: 548px; top: 330px;
    width: 2px; height: 190px; background: var(--divider);
  }
  .holder {
    position: absolute; right: 480px; top: 330px; text-align: right;
  }
  .holder-initials {
    font-weight: 700; font-size: 48px; color: var(--navy); line-height: 1;
    margin-bottom: 24px;
  }
  .holder-address {
    font-size: 22px; color: var(--text-grey); line-height: 1.4;
  }
  .contacts {
    position: absolute; left: 574px; top: 325px; list-style: none;
  }
  .contact-item {
    display: flex; align-items: center; gap: 14px;
    font-size: 22px; color: var(--text-grey); height: 42px;
  }
  .contact-icon { width: 22px; height: 22px; flex: none; }
</style>
</head>
<body>
  <div class="card">
    <div class="card-band"></div>
    <div class="card-band-line"></div>

    <div class="brand">
      <span class="brand-dot"></span>
      <span class="brand-name">Tallimora</span>
    </div>

    <div class="holder">
      <div class="holder-initials">RT</div>
      <div class="holder-address">
        Via G. Morelli, 17<br>
        26813 Codogno LO, Italy
      </div>
    </div>

    <div class="divider"></div>

    <ul class="contacts">
      <li class="contact-item">
        <svg class="contact-icon" viewBox="0 0 24 24"><path fill="#55585e" d="M6.6 10.8a15.1 15.1 0 0 0 6.6 6.6l2.2-2.2c.3-.3.7-.4 1-.2 1.1.4 2.3.6 3.6.6.6 0 1 .4 1 1V20c0 .6-.4 1-1 1A17 17 0 0 1 3 4c0-.6.4-1 1-1h3.5c.6 0 1 .4 1 1 0 1.3.2 2.5.6 3.6.1.3 0 .7-.2 1z"/></svg>
        +390241186320
      </li>
      <li class="contact-item">
        <svg class="contact-icon" viewBox="0 0 24 24"><rect x="4" y="3" width="16" height="6" rx="1" fill="#55585e"/><rect x="2" y="10" width="20" height="11" rx="2" fill="#55585e"/><rect x="6" y="14" width="12" height="3" fill="#fff"/></svg>
        +390241186321
      </li>
      <li class="contact-item">
        <svg class="contact-icon" viewBox="0 0 24 24"><circle cx="12" cy="12" r="4" fill="none" stroke="#55585e" stroke-width="2.4"/><path d="M16 8v5.5a2.5 2.5 0 0 0 5 0V12a9 9 0 1 0-3.5 7.1" fill="none" stroke="#55585e" stroke-width="2.4"/></svg>
        Info@Tallimora.com
      </li>
      <li class="contact-item">
        <svg class="contact-icon" viewBox="0 0 24 24"><g fill="none" stroke="#55585e" stroke-width="1.8"><circle cx="12" cy="12" r="9.5"/><ellipse cx="12" cy="12" rx="4" ry="9.5"/><path d="M2.5 12h19M4 7h16M4 17h16"/></g></svg>
        www.tallimora.com
      </li>
    </ul>
  </div>
</body>
</html>
```